Innovative Healthcare Technology Company needs a Business Card Design

We are in need of an innovative business card design for a new healthcare software company called "Lumenwise Data Partners". We develop software that creates medical assessment applications and mobile e-learning prevention services to reduce risk behaviors in adolescent and young adults. Our initial product, the "KESTREL App", conducts a tailored sexual risk assessment and provides a doctor with an insightful patient report to improve sexual risk counseling and ultimately reduce unintended pregnancy, STDs, etc.

We would like the design to incorporate our logo and branding colors (attached) in an innovative and creative manner. The final design should communicate professionalism and healthcare innovation. Our tag line is "CLARITY BEFORE CARE" (doesn't necessarily need to be included) and our target audience is doctors, medical directors, and medical business administrators. Please visit our website for additional info ourbrightmarq.com. Be creative and we look forward to seeing your designs!

Target Market(s)

healthcare - doctors, medical directors and medical business administrators

Industry/Entity Type

Healthcare

Contact Information for Business Card

We would like the design to incorporate our logo and branding colors (attached) in an innovative and creative manner. The final design should communicate professionalism and healthcare innovation. Our tag line is "CLARITY BEFORE CARE" (doesn't necessarily need to be included)

Font styles to use
Other font styles liked:
• quicksand

Requirements
Must have
• our logo and brand colors
• Name, (Mara Feldhovenik, PhD)
• Email (drmara@ourbrightmarq.com)
• phone (555.283.9170)
• Website (ourbrightmarq.com)
Should not have
• cartoon look

```html
<!DOCTYPE html>
<html lang="en">
<head>
<meta charset="utf-8">
<title>Lumenwise Data Partners – Business Card</title>
<link href="https://fonts.googleapis.com/css2?family=Quicksand:wght@400;500;600;700&display=swap" rel="stylesheet">
<style>
  :root {
    --bg: #3a3a3c;
    --paper: #ffffff;
    --brand-blue: #3b5f92;
    --brand-green: #7a9e82;
    --brand-gray: #8a8e8d;
    --brand-tan: #e3c9a6;
    --brand-purple: #8e8ab3;
    --tagline: #5a4a5e;
    --pattern-a: #ffffff;
    --pattern-b: #f1f2f4;
  }
  * { box-sizing: border-box; margin: 0; padding: 0; }
  html, body {
    width: 1200px; height: 900px; overflow: hidden;
    background: var(--bg);
    font-family: "Quicksand", sans-serif;
  }
  .canvas { position: relative; width: 1200px; height: 900px; }

  .card {
    position: absolute; left: 250px;
    width: 700px; height: 400px;
    background: var(--paper);
    overflow: hidden;
    box-shadow: 0 10px 28px rgba(0,0,0,.45);
  }
  .card--front { top: 40px; }
  .card--back { top: 470px; }

  .card__pattern {
    position: absolute; inset: 0;
    background: radial-gradient(ellipse at 75% 20%, var(--pattern-b), var(--pattern-a) 70%);
  }

  .brand { position: absolute; display: flex; align-items: flex-start; gap: 14px; color: var(--brand-blue); }
  .brand__square { width: 22px; height: 22px; background: var(--brand-blue); border-radius: 3px; margin-top: 14px; }
  .brand__name { font-weight: 600; line-height: 1; }
  .brand__name span { display: block; }
  .brand__main { font-size: 54px; letter-spacing: .5px; }
  .brand__sub { font-size: 26px; margin-top: 4px; letter-spacing: 1.5px; font-weight: 500; }

  .card--front .brand { left: 70px; top: 150px; }
  .tagline {
    position: absolute; left: 70px; top: 292px;
    font-size: 22px; font-weight: 500; letter-spacing: 2.5px;
    color: var(--tagline);
  }

  .stripe { position: absolute; left: 0; right: 0; bottom: 0; height: 16px; display: flex; }
  .stripe i { flex: 1; display: block; }
  .stripe .s-purple { background: var(--brand-purple); }
  .stripe .s-green { background: var(--brand-green); }
  .stripe .s-gray { background: var(--brand-gray); }
  .stripe .s-tan { background: var(--brand-tan); }

  .card--back .brand { left: 70px; top: 40px; }
  .card--back .brand__main { font-size: 46px; }
  .card--back .brand__sub { font-size: 22px; }

  .info-band {
    position: absolute; left: 0; right: 0; top: 180px; height: 200px;
    background: var(--brand-blue); color: #fff;
  }
  .person { position: absolute; left: 44px; top: 34px; font-size: 22px; font-weight: 700; letter-spacing: 1px; }
  .contact { position: absolute; right: 40px; top: 72px; list-style: none; }
  .contact li { display: flex; align-items: center; gap: 12px; font-size: 22px; font-weight: 500; letter-spacing: 1px; line-height: 34px; }
  .contact svg { width: 20px; height: 20px; flex: none; }
</style>
</head>
<body>
<main class="canvas">

  <section class="card card--front" aria-label="Card front">
    <div class="card__pattern" role="img" aria-label="Faint hexagonal molecule pattern"></div>
    <div class="brand">
      <div class="brand__square"></div>
      <div class="brand__name">
        <span class="brand__main">Lumenwise</span>
        <span class="brand__sub">Data Partners</span>
      </div>
    </div>
    <p class="tagline">CLARITY BEFORE CARE</p>
    <div class="stripe"><i class="s-purple"></i><i class="s-green"></i><i class="s-gray"></i><i class="s-tan"></i><i class="s-purple"></i></div>
  </section>

  <section class="card card--back" aria-label="Card back">
    <div class="card__pattern" role="img" aria-label="Faint hexagonal molecule pattern"></div>
    <div class="brand">
      <div class="brand__square"></div>
      <div class="brand__name">
        <span class="brand__main">Lumenwise</span>
        <span class="brand__sub">Data Partners</span>
      </div>
    </div>
    <div class="info-band">
      <p class="person">Mara Feldhovenik, PhD</p>
      <ul class="contact">
        <li>
          <svg viewBox="0 0 20 20" aria-hidden="true"><rect x="2" y="5" width="16" height="11" fill="none" stroke="#7a9e82" stroke-width="2"/><path d="M2 5l8 6 8-6" fill="none" stroke="#7a9e82" stroke-width="2"/></svg>
          drmara@ourbrightmarq.com
        </li>
        <li>
          <svg viewBox="0 0 20 20" aria-hidden="true"><path d="M5 2l3 4-2 2c1 2.5 3 4.5 5.5 5.5l2-2 4 3-2 3C9 17 3 11 2 4z" fill="#7a9e82"/></svg>
          555.283.9170
        </li>
        <li>
          <svg viewBox="0 0 20 20" aria-hidden="true"><circle cx="10" cy="10" r="8" fill="none" stroke="#7a9e82" stroke-width="2"/><path d="M2 10h16M10 2c-4 4-4 12 0 16M10 2c4 4 4 12 0 16" fill="none" stroke="#7a9e82" stroke-width="1.5"/></svg>
          ourbrightmarq.com
        </li>
      </ul>
    </div>
    <div class="stripe"><i class="s-purple"></i><i class="s-green"></i><i class="s-gray"></i><i class="s-tan"></i><i class="s-purple"></i></div>
  </section>

</main>
</body>
</html>
```